Life Coach for Lawyers Business Card Design

Elegant, original, business card design for life coaching service for associate attorneys who work in big law and struggle with stress, overwhelm, and time management. Double sided design.

Target Market(s)

Women associate attorneys who work in big law and struggle with stress, overwhelm, and time management.

Industry/Entity Type

Life Coaching

Contact Information for Business Card

Marissa Pendrell
Life Coach
518.677.3941
calmbriefcounsel.net
marissa@calmbriefcounsel.net
@calmbriefcounsel (Instagram)

Font styles to use
Other font styles liked:
• Silver South font duo. See uploaded files.

Requirements
Must have
• Icons for phone, website, email, and Instagram instead of words. Specific colors used in my logo (171B2B, 421121, FFFFFF)
Nice to have
• Foil. Embossed. Feminine design.
Should not have
• Any colors other than those used in logo. See uploaded files.

```html
<!DOCTYPE html>
<html lang="en">
<head>
<meta charset="utf-8">
<title>Calm Brief Counsel – Business Card</title>
<link rel="stylesheet" href="https://fonts.googleapis.com/css2?family=Cormorant+Garamond:wght@500&family=Montserrat:wght@300;400&family=Mrs+Saint+Delafield&display=swap">
<style>
  :root {
    --wine: #421121;
    --ink: #171B2B;
    --paper: #FFFFFF;
    --backdrop: #9c9c9c;
    --wine-soft: #7a4a58;
  }
  * { box-sizing: border-box; margin: 0; padding: 0; }
  html, body {
    width: 1200px; height: 1162px; overflow: hidden;
    background: var(--backdrop);
  }
  .canvas {
    width: 1200px; height: 1162px;
    display: flex; flex-direction: column; align-items: center;
    justify-content: center; gap: 60px;
  }
  .card {
    width: 860px; height: 491px; position: relative;
    box-shadow: 0 18px 40px rgba(0,0,0,0.25);
  }
  .card--front { background: var(--paper); color: var(--wine); }
  .card--back { background: var(--wine); color: var(--paper); display: flex; align-items: center; justify-content: center; }

  .card__name {
    position: absolute; left: 70px; top: 40px;
    font-family: "Mrs Saint Delafield", cursive;
    font-size: 104px; line-height: 1; color: var(--wine);
  }
  .card__brand {
    position: absolute; right: 60px; top: 150px;
    display: flex; align-items: center; gap: 10px;
  }
  .card__brand-dot {
    width: 14px; height: 14px; border-radius: 50%;
    border: 1.5px solid var(--wine);
  }
  .card__brand-name {
    font-family: "Cormorant Garamond", serif; font-weight: 500;
    font-size: 16px; letter-spacing: 2px; text-transform: uppercase;
    color: var(--wine);
  }
  .contact {
    position: absolute; left: 70px; top: 268px;
    list-style: none;
    font-family: "Montserrat", sans-serif; font-weight: 300;
    font-size: 21px; color: var(--ink); letter-spacing: 0.5px;
  }
  .contact__item { display: flex; align-items: center; gap: 14px; height: 34px; }
  .contact__icon { width: 22px; height: 22px; flex: none; }
  .card__title {
    position: absolute; right: 70px; bottom: 58px;
    font-family: "Cormorant Garamond", serif; font-weight: 500;
    font-size: 34px; letter-spacing: 1px; color: var(--wine);
  }
  .brand-mark {
    font-family: "Cormorant Garamond", serif; font-weight: 500;
    font-size: 78px; line-height: 1.05; letter-spacing: 6px;
    text-transform: uppercase; text-align: center; color: var(--paper);
  }
</style>
</head>
<body>
<main class="canvas">
  <section class="card card--front" aria-label="Card front">
    <h1 class="card__name">Marissa Pendrell</h1>
    <div class="card__brand">
      <span class="card__brand-dot"></span>
      <span class="card__brand-name">Calm Brief Counsel</span>
    </div>
    <ul class="contact">
      <li class="contact__item">
        <svg class="contact__icon" viewBox="0 0 22 22" aria-hidden="true"><circle cx="11" cy="11" r="10" fill="none" stroke="#421121" stroke-width="1.2"/><path d="M8 6.5c-.6 0-1.3.7-1.3 1.5 0 3.5 3.8 7.3 7.3 7.3.8 0 1.5-.7 1.5-1.3l-1.8-1.4-1.2.9c-1.3-.6-2.4-1.7-3-3l.9-1.2z" fill="#421121"/></svg>
        <span>518.677.3941</span>
      </li>
      <li class="contact__item">
        <svg class="contact__icon" viewBox="0 0 22 22" aria-hidden="true"><circle cx="11" cy="11" r="10" fill="none" stroke="#421121" stroke-width="1.2"/><rect x="6" y="7.5" width="10" height="7" fill="none" stroke="#421121" stroke-width="1.2"/><path d="M6 7.5l5 4 5-4" fill="none" stroke="#421121" stroke-width="1.2"/></svg>
        <span>marissa@calmbriefcounsel.net</span>
      </li>
      <li class="contact__item">
        <svg class="contact__icon" viewBox="0 0 22 22" aria-hidden="true"><circle cx="11" cy="11" r="10" fill="none" stroke="#421121" stroke-width="1.2"/><circle cx="11" cy="11" r="5.5" fill="none" stroke="#421121" stroke-width="1"/><ellipse cx="11" cy="11" rx="2.3" ry="5.5" fill="none" stroke="#421121" stroke-width="1"/><path d="M5.5 11h11" stroke="#421121" stroke-width="1"/></svg>
        <span>calmbriefcounsel.net</span>
      </li>
      <li class="contact__item">
        <svg class="contact__icon" viewBox="0 0 22 22" aria-hidden="true"><circle cx="11" cy="11" r="10" fill="none" stroke="#421121" stroke-width="1.2"/></svg>
        <span>@calmbriefcounsel</span>
      </li>
    </ul>
    <p class="card__title">LIFE COACH</p>
  </section>

  <section class="card card--back" aria-label="Card back">
    <p class="brand-mark">Calm Brief<br>Counsel</p>
  </section>
</main>
</body>
</html>
```